Online interactive calendar for training organisation

We have a new website being made and need a design for an online calendar that is interactive and very simple and easy to use. On our main page this calendar will include all of our courses (approx 30 different ones with up to 8 different locations). On our sub pages which have course information, the calendar will only include details of that specific course. Details needed are: Course code, course name/title, date, duration (1/2 day - 5 days), location, price, discount price. Maybe also a key for available or limited spots left? We want a section at the top of the calendar to be able to filter by location or course, and maybe to filter by month also? I have included a spreadsheet with a sample of our courses with this information. Also a sample draft of the main page on our new webpage to show the colour green which is our company colour. Main notes - we want as simple, effective and easy to use as possible.
We will need to know what plug in we can use to get the design you have created.

Target Market(s)

Mining and construction - both companies and individuals

Number of Pages Required

1 page

Colors
cadf82

Requirements
Must have
• Be simple, easy to use, effective.

```html
<!DOCTYPE html>
<html lang="en">
<head>
<meta charset="utf-8">
<title>Ridgeline Safety – Course Calendar</title>
<link href="https://fonts.googleapis.com/css2?family=Montserrat:wght@500;600;700&family=Fira+Sans:wght@400;500&family=Lato:wght@400;700&display=swap" rel="stylesheet">
<style>
:root{
  --brand:#cadf82;
  --brand-strong:#9ccb3b;
  --ink:#2a2a2a;
  --muted:#555;
  --sale:#e8231f;
  --line:#c9c9c9;
  --page:#f4f4f4;
  --panel:#efefef;
  --footer:#2c2c2c;
}
*{box-sizing:border-box;margin:0;padding:0}
html,body{width:1200px;height:2618px;overflow:hidden}
body{position:relative;background:var(--page);font-family:"Fira Sans",sans-serif;color:var(--ink)}
.abs{position:absolute}

/* calendar block */
.calendar{position:absolute;width:1000px;height:620px}
.calendar-title{position:absolute;left:0;width:1000px;top:38px;text-align:center;font:700 32px "Montserrat",sans-serif;color:var(--ink)}
.filter{position:absolute;top:128px;width:210px;height:49px;background:var(--brand);font:500 23px "Montserrat",sans-serif;color:#3a3a3a;display:flex;align-items:center;justify-content:center;padding-right:30px;z-index:2}
.filter::after{content:"";position:absolute;right:14px;top:21px;border-left:8px solid transparent;border-right:8px solid transparent;border-top:9px solid #333}
.board{position:absolute;left:65px;top:175px;width:977px;height:417px;border:1px solid #333}
.card{position:absolute;width:310px;height:153px;background:#fff;border:1px solid var(--line);box-shadow:0 1px 3px rgba(0,0,0,.12)}
.card-head{position:absolute;left:0;top:0;width:100%;height:51px;border-bottom:1px solid #e3e3e3}
.duration{position:absolute;left:8px;top:4px;width:44px;height:44px;border-radius:50%;background:var(--brand);font-size:14px;display:flex;align-items:center;justify-content:center;color:#333}
.duration.small{font-size:12px}
.date{position:absolute;right:0;top:0;height:31px;padding:0 5px 0 10px;background:var(--brand);font-size:12px;display:flex;align-items:center;gap:8px;color:#333}
.title{position:absolute;left:33px;right:10px;top:51px;height:48px;border-bottom:1px solid #e3e3e3;display:flex;align-items:center;font:500 14px "Fira Sans",sans-serif;line-height:18px;color:#333}
.title.wide{left:12px}
.title.wide + .meta{left:12px}
.star{color:var(--sale);font-size:14px;margin-left:3px;align-self:flex-start;margin-top:10px}
.meta{position:absolute;left:34px;right:24px;top:99px;height:52px;display:flex;align-items:center;font-size:16px;color:#333}
.meta .price{margin-left:auto;font-size:17px}
.meta .was{text-decoration:line-through;color:#333;margin-right:14px}
.meta .now{color:var(--sale)}
.key{position:absolute;left:0;width:977px;bottom:8px;text-align:center;font-size:19px;color:#444}
.key b{color:var(--sale);font-weight:400;margin-right:12px}

/* site header */
.topbar{position:absolute;left:0;top:773px;width:1200px;height:32px;background:var(--brand-strong)}
.social{position:absolute;top:8px;display:flex;gap:5px}
.social i{width:18px;height:18px;border-radius:50%;background:#111;display:block}
.student{position:absolute;left:782px;top:6px;width:84px;height:20px;background:#1d1d1d;color:#fff;font:700 9px "Lato",sans-serif;display:flex;align-items:center;justify-content:center;border-radius:2px}
.search{position:absolute;left:873px;top:6px;width:108px;height:20px;background:#fff;border-radius:2px}
.masthead{position:absolute;left:0;top:805px;width:1200px;height:81px;background:#fff}
.brand{position:absolute;left:223px;top:18px;display:flex;align-items:center;gap:10px}
.brand-mark{width:38px;height:38px;border-radius:50%;background:var(--sale)}
.brand-name{font:700 22px "Lato",sans-serif;color:var(--sale);letter-spacing:1px}
.nav{position:absolute;left:618px;top:34px;display:flex;gap:18px;font:400 9.5px "Lato",sans-serif;color:#333}
.nav .on{color:var(--brand-strong)}

/* difference */
.difference{position:absolute;left:0;top:886px;width:1200px;height:449px;background:var(--panel)}
.difference h2{position:absolute;top:40px;width:1200px;text-align:center;font:400 26px "Lato",sans-serif;color:#222}
.difference p{position:absolute;top:73px;width:1200px;text-align:center;font-size:10px;color:#444}
.rule{position:absolute;left:580px;top:96px;width:40px;height:2px;background:var(--brand)}
.tile{position:absolute;width:115px;height:112px}
.tile-label{position:absolute;width:140px;text-align:center;font:400 10px "Lato",sans-serif;color:#333}
.calendar-band{position:absolute;left:0;top:1335px;width:1200px;height:686px;background:#fff}

/* hero */
.hero{position:absolute;left:0;top:2021px;width:1200px;height:414px;background:linear-gradient(90deg,#7a6d3e 0%,#c9a93a 25%,#a39a85 45%,#e6e4e0 65%,#f2f2f0 100%)}
.hero-frame{position:absolute;left:765px;top:66px;width:250px;height:285px;border:14px solid #fff}
.hero-title{position:absolute;left:650px;top:150px;font:700 40px "Fira Sans",sans-serif;line-height:44px;color:#262626}
.hero-tag{position:absolute;left:650px;top:247px;width:330px;height:24px;background:var(--brand-strong);color:#fff;font-size:10.5px;display:flex;align-items:center;justify-content:center}

/* footer */
.footer{position:absolute;left:0;top:2435px;width:1200px;height:148px;background:var(--footer)}
.footer .brand{left:290px;top:40px}
.footer .brand-mark{width:30px;height:30px}
.footer .brand-name{font-size:18px}
.follow{position:absolute;left:325px;top:88px;display:flex;align-items:center;gap:5px;font:400 9.5px "Lato",sans-serif;color:#ddd}
.follow i{width:14px;height:14px;background:#fff;display:block;border-radius:2px}
.fnav{position:absolute;left:615px;top:57px;display:flex;gap:14px;font:400 8px "Lato",sans-serif;color:#ddd}
.contact{position:absolute;top:85px;display:flex;align-items:center;gap:10px;font:400 8.5px "Lato",sans-serif;color:#ddd}
.contact span.ic{width:18px;height:18px;background:#111;display:flex;align-items:center;justify-content:center}
.to-top{position:absolute;left:940px;top:130px;width:30px;height:30px;background:#fff;border:1px solid #ccc;display:flex;align-items:center;justify-content:center;z-index:3}
.copybar{position:absolute;left:0;top:2583px;width:1200px;height:35px;background:var(--brand-strong);text-align:center;font:400 8px "Lato",sans-serif;color:#333;padding-top:15px}
</style>
</head>
<body>

<div class="abs" style="left:57px;top:70px;width:1088px;height:627px;background:#fff;border:1px solid #e8e8e8"></div>

<!-- calendar (main page) -->
<section class="calendar" style="left:56px;top:70px">
  <h1 class="calendar-title" style="left:54px">Calendar</h1>
  <div class="filter" style="left:156px">Ridgeway</div>
  <div class="filter" style="left:449px">COURSE</div>
  <div class="filter" style="left:741px">MONTH</div>
  <div class="board">
    <article class="card" style="left:9px;top:34px">
      <div class="card-head"><span class="duration">1 day</span><span class="date"><svg width="12" height="12" viewBox="0 0 12 12"><rect x="1" y="2" width="10" height="9" fill="none" stroke="#555"/><path d="M1 5h10M4 1v2M8 1v2" stroke="#555"/></svg>Tuesday, October 29, 2019</span></div>
      <div class="title">RIIHAN304D Work safely at heights<span class="star">*</span></div>
      <div class="meta">8 Am<span class="price"><span class="was">$ 500.00</span><span class="now">$ 120.00</span></span></div>
    </article>
    <article class="card" style="left:335px;top:34px">
      <div class="card-head"><span class="duration small">1/2 day</span><span class="date"><svg width="12" height="12" viewBox="0 0 12 12"><rect x="1" y="2" width="10" height="9" fill="none" stroke="#555"/><path d="M1 5h10M4 1v2M8 1v2" stroke="#555"/></svg>Thursday, January 30, 2020</span></div>
      <div class="title wide">HLTAID005 Confined space - practical only (theory online)</div>
      <div class="meta">1pm<span class="price">$ 80.00</span></div>
    </article>
    <article class="card" style="left:658px;top:34px">
      <div class="card-head"><span class="duration">1 day</span><span class="date"><svg width="12" height="12" viewBox="0 0 12 12"><rect x="1" y="2" width="10" height="9" fill="none" stroke="#555"/><path d="M1 5h10M4 1v2M8 1v2" stroke="#555"/></svg>Tuesday, October 29, 2019</span></div>
      <div class="title">RIIHAN304D Work safely at heights<span class="star" style="margin-left:14px">*</span></div>
      <div class="meta">8 Am<span class="price"><span class="was">$ 500.00</span><span class="now">$ 120.00</span></span></div>
    </article>
    <article class="card" style="left:9px;top:212px">
      <div class="card-head"><span class="duration">1 day</span><span class="date"><svg width="12" height="12" viewBox="0 0 12 12"><rect x="1" y="2" width="10" height="9" fill="none" stroke="#555"/><path d="M1 5h10M4 1v2M8 1v2" stroke="#555"/></svg>Friday, November 15, 2019</span></div>
      <div class="title">HLTAID001 First Aid - practical only</div>
      <div class="meta">1pm<span class="price">$ 80.00</span></div>
    </article>
    <article class="card" style="left:335px;top:212px">
      <div class="card-head"><span class="duration small">10 days</span><span class="date"><svg width="12" height="12" viewBox="0 0 12 12"><rect x="1" y="2" width="10" height="9" fill="none" stroke="#555"/><path d="M1 5h10M4 1v2M8 1v2" stroke="#555"/></svg>Monday, October 28, 2019</span></div>
      <div class="title wide">CPCCCM208 Dogging &amp; TLILIC0005 front end loader BUNDLE</div>
      <div class="meta">8 am<span class="price"><span class="was">$ 2,300.00</span><span class="now">$ 1,200.00</span></span></div>
    </article>
    <p class="key"><b>*</b>limited spots left</p>
  </div>
</section>

<!-- site header -->
<div class="topbar">
  <div class="social" style="left:221px"><i></i><i></i><i></i><i></i></div>
  <div class="student">Student Access</div>
  <div class="search"><svg class="abs" style="left:89px;top:5px" width="10" height="10" viewBox="0 0 10 10"><circle cx="4" cy="4" r="3" fill="none" stroke="#222" stroke-width="1.5"/><path d="M6.3 6.3L9 9" stroke="#222" stroke-width="1.5"/></svg></div>
</div>
<header class="masthead">
  <div class="brand"><span class="brand-mark"></span><span class="brand-name">RIDGELINE SAFETY</span></div>
  <nav class="nav"><span class="on">Home</span><span>Courses</span><span>Our Services</span><span>About us</span><span>Funding</span><span>Locations</span><span>Contact us</span></nav>
</header>

<section class="difference">
  <h2>THE RIDGELINE SAFETY DIFFERENCE</h2>
  <p>Committed to helping our students succeed.</p>
  <div class="rule"></div>
  <div class="tile" style="left:288px;top:123px;background:linear-gradient(135deg,#6d6a63,#b89a3c)" role="img" aria-label="Loader on a quarry stockpile"></div>
  <div class="tile" style="left:413px;top:123px;background:linear-gradient(135deg,#6fa3d6,#e8c64a)" role="img" aria-label="Handshake in work gloves"></div>
  <div class="tile" style="left:541px;top:123px;background:linear-gradient(135deg,#8a8a86,#c6343a)" role="img" aria-label="Tipper truck at a mine site"></div>
  <div class="tile" style="left:670px;top:123px;background:linear-gradient(135deg,#7e7b74,#d6a330)" role="img" aria-label="Excavator on rough ground"></div>
  <div class="tile" style="left:798px;top:123px;background:linear-gradient(135deg,#b9c6cf,#4f5a52)" role="img" aria-label="Workers harnessed at height"></div>
  <div class="tile-label" style="left:276px;top:246px">All Courses</div>
  <div class="tile-label" style="left:401px;top:246px">Funded courses</div>
  <div class="tile-label" style="left:529px;top:246px">Mining</div>
  <div class="tile-label" style="left:658px;top:246px">Standard 11</div>
  <div class="tile-label" style="left:786px;top:246px">Work safely at heights</div>
  <div class="tile" style="left:288px;top:275px;background:linear-gradient(135deg,#5a6a7a,#2d2d33)" role="img" aria-label="Office team at a laptop"></div>
  <div class="tile" style="left:413px;top:275px;background:linear-gradient(135deg,#d9b26b,#4d8ac1)" role="img" aria-label="Students studying online"></div>
  <div class="tile" style="left:541px;top:275px;background:linear-gradient(135deg,#a7c7e0,#d8d25a)" role="img" aria-label="Site engineers reviewing plans"></div>
  <div class="tile" style="left:670px;top:275px;background:linear-gradient(135deg,#7b8da3,#e2c22c)" role="img" aria-label="Elevated work platform"></div>
  <div class="tile" style="left:798px;top:275px;background:linear-gradient(135deg,#6f7f8e,#c97a3a)" role="img" aria-label="Construction worker on site"></div>
  <div class="tile-label" style="left:276px;top:398px">Corporate clients</div>
  <div class="tile-label" style="left:401px;top:398px">Online courses</div>
  <div class="tile-label" style="left:529px;top:398px">RPL's &amp; VOC's</div>
  <div class="tile-label" style="left:658px;top:398px">Plant &amp; Equipment</div>
  <div class="tile-label" style="left:786px;top:398px">Construction</div>
</section>

<div class="calendar-band"></div>

<!-- calendar (course page) -->
<section class="calendar" style="left:46px;top:1350px">
  <h1 class="calendar-title" style="left:54px">Calendar</h1>
  <div class="filter" style="left:156px">Ridgeway</div>
  <div class="filter" style="left:449px">COURSE</div>
  <div class="filter" style="left:741px">MONTH</div>
  <div class="board">
    <article class="card" style="left:9px;top:34px">
      <div class="card-head"><span class="duration">1 day</span><span class="date"><svg width="12" height="12" viewBox="0 0 12 12"><rect x="1" y="2" width="10" height="9" fill="none" stroke="#555"/><path d="M1 5h10M4 1v2M8 1v2" stroke="#555"/></svg>Tuesday, October 29, 2019</span></div>
      <div class="title">RIIHAN304D Work safely at heights<span class="star">*</span></div>
      <div class="meta">8 Am<span class="price"><span class="was">$ 500.00</span><span class="now">$ 120.00</span></span></div>
    </article>
    <article class="card" style="left:335px;top:34px">
      <div class="card-head"><span class="duration small">1/2 day</span><span class="date"><svg width="12" height="12" viewBox="0 0 12 12"><rect x="1" y="2" width="10" height="9" fill="none" stroke="#555"/><path d="M1 5h10M4 1v2M8 1v2" stroke="#555"/></svg>Thursday, January 30, 2020</span></div>
      <div class="title wide">HLTAID005 Confined space - practical only (theory online)</div>
      <div class="meta">1pm<span class="price">$ 80.00</span></div>
    </article>
    <article class="card" style="left:658px;top:34px">
      <div class="card-head"><span class="duration">1 day</span><span class="date"><svg width="12" height="12" viewBox="0 0 12 12"><rect x="1" y="2" width="10" height="9" fill="none" stroke="#555"/><path d="M1 5h10M4 1v2M8 1v2" stroke="#555"/></svg>Tuesday, October 29, 2019</span></div>
      <div class="title">RIIHAN304D Work safely at heights<span class="star" style="margin-left:14px">*</span></div>
      <div class="meta">8 Am<span class="price"><span class="was">$ 500.00</span><span class="now">$ 120.00</span></span></div>
    </article>
    <article class="card" style="left:9px;top:212px">
      <div class="card-head"><span class="duration">1 day</span><span class="date"><svg width="12" height="12" viewBox="0 0 12 12"><rect x="1" y="2" width="10" height="9" fill="none" stroke="#555"/><path d="M1 5h10M4 1v2M8 1v2" stroke="#555"/></svg>Friday, November 15, 2019</span></div>
      <div class="title">HLTAID001 First Aid - practical only</div>
      <div class="meta">1pm<span class="price">$ 80.00</span></div>
    </article>
    <article class="card" style="left:335px;top:212px">
      <div class="card-head"><span class="duration small">10 days</span><span class="date"><svg width="12" height="12" viewBox="0 0 12 12"><rect x="1" y="2" width="10" height="9" fill="none" stroke="#555"/><path d="M1 5h10M4 1v2M8 1v2" stroke="#555"/></svg>Monday, October 28, 2019</span></div>
      <div class="title wide">CPCCCM208 Dogging &amp; TLILIC0005 front end loader BUNDLE</div>
      <div class="meta">8 am<span class="price"><span class="was">$ 2,300.00</span><span class="now">$ 1,200.00</span></span></div>
    </article>
    <p class="key"><b>*</b>limited spots left</p>
  </div>
</section>

<!-- hero -->
<section class="hero" role="img" aria-label="Large yellow haul truck on a mine site">
  <div class="hero-frame"></div>
  <h2 class="hero-title">Training a Safety<br>Culture that Counts</h2>
  <div class="hero-tag">NOW TRAINING - Working at Heights &amp; Confined Spaces courses</div>
</section>

<footer class="footer">
  <div class="brand"><span class="brand-mark"></span><span class="brand-name">RIDGELINE SAFETY</span></div>
  <div class="follow">Follow us on :- <i></i><i></i><i></i><i></i></div>
  <nav class="fnav"><span>Home</span><span>Courses</span><span>Our Services</span><span>About us</span><span>Funding</span><span>Locations</span><span>Contact us</span></nav>
  <div class="contact" style="left:590px"><span class="ic"><svg width="9" height="11" viewBox="0 0 9 11"><path d="M4.5 0.5a4 4 0 0 1 4 4c0 3-4 6-4 6s-4-3-4-6a4 4 0 0 1 4-4z" fill="#fff"/><circle cx="4.5" cy="4.5" r="1.4" fill="#111"/></svg></span>18 Quarry Road, Ridgeway QLD 4300</div>
  <div class="contact" style="left:790px"><span class="ic"><svg width="11" height="8" viewBox="0 0 11 8"><rect width="11" height="8" fill="#fff"/><path d="M0 0l5.5 4.5L11 0" fill="none" stroke="#111"/></svg></span>info@ridgelinesafety.edu.au</div>
  <div class="to-top"><svg width="12" height="8" viewBox="0 0 12 8"><path d="M1 7l5-5 5 5" fill="none" stroke="#222" stroke-width="1.6"/></svg></div>
</footer>
<div class="copybar">© Copyright All Right Reserved | Powered by Ridgeline Safety.</div>

</body>
</html>
```